Website design for an Italian restaurant in Amsterdam

I need a design for a client of mine. It is for Teatro Lunaverde, an Italian restaurant in Amsterdam.
We are going for a clean, modern look but we also need to realise an authentic feel.
The restaurant is located in an old movie theatre, that is where the name Teatro Lunaverde comes from.
Industry/Entity Type
Italian Restaurant
Number of Pages Required
1 page
Font styles to use
Sans Serif
Colors
Designer to choose colors to be used in the design.

```html
<!DOCTYPE html>
<html lang="en">
<head>
<meta charset="utf-8">
<title>Teatro Lunaverde — Italian Restaurant in Amsterdam</title>
<link rel="stylesheet" href="https://fonts.googleapis.com/css2?family=Lora:ital,wght@0,400;0,500;0,700;1,400&display=swap">
<style>
  :root {
    --orange: #f7941d;
    --ink: #1c1c1c;
    --muted: #8a8a8a;
    --light-bg: #efefef;
    --white: #ffffff;
    --dark: #0d0a08;
    --line: #d9c9a8;
    --serif: "Lora", Georgia, serif;
  }
  * { box-sizing: border-box; margin: 0; padding: 0; }
  html, body { width: 1200px; height: 3939px; overflow: hidden; }
  body { position: relative; background: var(--white); font-family: var(--serif); color: var(--ink); }
  .abs { position: absolute; }

  /* Header */
  .site-header { position: absolute; left: 0; top: 0; width: 1200px; height: 100px; background: var(--white); }
  .brand { position: absolute; left: 22px; top: 30px; display: flex; align-items: center; gap: 10px; }
  .brand-square { width: 20px; height: 20px; background: var(--ink); }
  .brand-name { font-size: 15px; font-weight: 700; letter-spacing: 2px; color: var(--ink); }
  .main-nav { position: absolute; left: 418px; top: 40px; display: flex; gap: 0; font-size: 13px; text-transform: uppercase; }
  .main-nav a { color: var(--ink); text-decoration: none; padding: 0 12px; position: relative; }
  .main-nav a + a::before { content: "·"; position: absolute; left: -3px; color: var(--muted); }
  .btn-book { position: absolute; left: 1027px; top: 29px; width: 157px; height: 42px; border: 1px solid var(--ink); display: flex; align-items: center; justify-content: center; gap: 18px; font-size: 13px; text-transform: uppercase; }

  /* Hero */
  .hero { position: absolute; left: 0; top: 100px; width: 1200px; height: 499px; overflow: hidden;
    background: linear-gradient(180deg, #1a3fb8 0%, #2a55d6 35%, #5a4a6a 62%, #c88a3a 80%, #3a2410 100%); }
  .hero-glow { position: absolute; left: 380px; top: 120px; width: 780px; height: 380px;
    background: radial-gradient(ellipse at 50% 60%, rgba(255,190,90,.75), rgba(160,90,30,.35) 55%, transparent 75%); }
  .hero-kicker { position: absolute; left: 118px; top: 186px; font-size: 17px; line-height: 22px; color: var(--white); text-transform: uppercase; }
  .hero-title { position: absolute; left: 118px; top: 240px; font-size: 44px; line-height: 56px; color: var(--white); font-weight: 500; text-transform: uppercase; letter-spacing: 1px; }
  .btn-learn { position: absolute; left: 118px; top: 373px; width: 121px; height: 39px; border-radius: 20px; background: var(--orange); color: var(--white); font-size: 12px; text-transform: uppercase; display: flex; align-items: center; justify-content: center; }
  .hero-call { position: absolute; left: 118px; top: 450px; font-size: 18px; line-height: 25px; color: var(--white); text-transform: uppercase; }
  .hero-dots { position: absolute; left: 582px; top: 550px; display: flex; gap: 6px; }
  .hero-dots span { width: 8px; height: 8px; border-radius: 50%; background: rgba(255,255,255,.55); }
  .hero-dots span:first-child { background: var(--white); }
  .hero-arrow { position: absolute; left: 589px; top: 490px; }

  /* About */
  .about { position: absolute; left: 0; top: 599px; width: 1200px; height: 672px; background: var(--light-bg); }
  .about-title { position: absolute; left: 200px; top: 120px; font-size: 31px; line-height: 38px; color: var(--orange); font-weight: 400; }
  .about-tagline { position: absolute; left: 200px; top: 280px; font-size: 19px; font-style: italic; color: var(--ink); }
  .about-text { position: absolute; left: 200px; top: 322px; width: 360px; font-size: 11.5px; line-height: 16px; color: var(--muted); }
  .about-badge { position: absolute; left: 200px; top: 459px; width: 55px; height: 58px; border: 2px solid var(--ink); border-radius: 8px; background: var(--white); }
  .about-link { position: absolute; left: 268px; top: 473px; font-size: 11px; text-transform: uppercase; color: var(--muted); border-bottom: 1px solid var(--muted); padding-bottom: 4px; }
  .about-photo { position: absolute; left: 635px; top: 89px; width: 363px; height: 481px;
    background: linear-gradient(160deg, #e8e6e2 0%, #cfcbc4 35%, #9e958a 65%, #4a4038 100%); }

  /* Section headings */
  .section-title { position: absolute; left: 0; width: 1200px; text-align: center; font-size: 46px; font-weight: 400; color: var(--ink); }

  /* Menu cards */
  .dish { position: absolute; width: 305px; }
  .dish-photo { width: 305px; height: 231px; }
  .dish-new { position: absolute; right: 11px; top: -31px; width: 62px; height: 62px; border-radius: 50%; background: var(--white); display: flex; align-items: flex-end; justify-content: center; padding-bottom: 10px; font-size: 13px; font-style: italic; }
  .dish-name { margin-top: 18px; font-size: 17px; color: var(--orange); }
  .dish-desc { margin-top: 4px; font-size: 12px; line-height: 16px; color: var(--muted); width: 170px; }
  .btn-menu { position: absolute; left: 520px; top: 2200px; width: 155px; height: 43px; border: 1px solid var(--ink); display: flex; align-items: center; justify-content: center; gap: 30px; font-size: 13px; text-transform: uppercase; }

  /* Gallery */
  .gallery-tile { position: absolute; width: 230px; height: 202px; }

  /* Booking */
  .booking { position: absolute; left: 0; top: 3041px; width: 1200px; height: 517px;
    background: radial-gradient(ellipse at 30% 40%, #5a3a1c 0%, #2a1a0e 40%, #0b0806 80%); }
  .booking-title { position: absolute; left: 0; top: 113px; width: 1200px; text-align: center; font-size: 29px; color: var(--white); }
  .field { position: absolute; border: 1px solid rgba(255,255,255,.35); color: rgba(255,255,255,.75); font-size: 12px; padding: 10px 12px; }
  .btn-submit { position: absolute; left: 499px; top: 370px; width: 158px; height: 42px; background: var(--orange); color: var(--white); font-size: 12px; text-transform: uppercase; display: flex; align-items: center; justify-content: center; }

  /* Footer */
  .footer-col { position: absolute; top: 3657px; font-size: 12px; line-height: 22px; color: var(--ink); }
  .footer-col h4 { font-size: 14px; font-weight: 700; margin-bottom: 14px; }
  .footer-col p { line-height: 16px; }
  .social { display: flex; gap: 14px; margin-top: 4px; }
  .social span { width: 18px; height: 18px; border-radius: 50%; background: #6d6d6d; }
  .copyright { position: absolute; left: 0; top: 3894px; width: 1200px; height: 45px; background: var(--dark); color: var(--white); font-size: 11px; display: flex; align-items: center; justify-content: center; }
</style>
</head>
<body>

<header class="site-header">
  <div class="brand"><span class="brand-square"></span><span class="brand-name">TEATRO LUNAVERDE</span></div>
  <nav class="main-nav">
    <a href="#">Home</a><a href="#">About</a><a href="#">Menu</a><a href="#">Blog</a><a href="#">Gallery</a><a href="#">Contacts</a>
  </nav>
  <div class="btn-book">Book Now
    <svg width="8" height="12" viewBox="0 0 8 12"><path d="M1 1l5 5-5 5" fill="none" stroke="#1c1c1c" stroke-width="2"/></svg>
  </div>
</header>

<section class="hero" role="img" aria-label="Evening view of old Amsterdam canal houses lit in warm light under a deep blue sky">
  <div class="hero-glow"></div>
  <p class="hero-kicker">Welcome to, Italian<br>restaurant in Amsterdam</p>
  <h1 class="hero-title">Teatro<br>Lunaverde</h1>
  <div class="btn-learn">Learn more</div>
  <p class="hero-call">For reservation call<br>+31 20 555 0147</p>
  <svg class="hero-arrow" width="22" height="14" viewBox="0 0 22 14"><path d="M2 2l9 9 9-9" fill="none" stroke="rgba(255,255,255,.7)" stroke-width="2"/></svg>
  <div class="hero-dots"><span></span><span></span><span></span><span></span></div>
</section>

<section class="about">
  <svg class="abs" style="left:118px;top:57px" width="66" height="66"><line x1="0" y1="0" x2="66" y2="66" stroke="var(--line)" stroke-width="1.5"/></svg>
  <svg class="abs" style="left:118px;top:530px" width="66" height="66"><line x1="0" y1="66" x2="66" y2="0" stroke="var(--line)" stroke-width="1.5"/></svg>
  <svg class="abs" style="left:1014px;top:57px" width="66" height="66"><line x1="0" y1="0" x2="66" y2="66" stroke="var(--line)" stroke-width="1.5"/></svg>
  <svg class="abs" style="left:1014px;top:530px" width="66" height="66"><line x1="0" y1="66" x2="66" y2="0" stroke="var(--line)" stroke-width="1.5"/></svg>
  <h2 class="about-title">About &nbsp;Teatro<br>Lunaverde<br>Italian restaurant<br>in Amsterdam</h2>
  <p class="about-tagline">The Italian restaurant to enjoy life and food.</p>
  <p class="about-text">Nemo enim ipsam voluptatem quia voluptas sit aspernatur aut odit aut fugit, sed quia consequuntur magni dolores eos qui ratione voluptatem sequi nesciunt. Neque porro quisquam est, qui dolorem ipsum quia dolor sit amet, consectetur, adipisci velit, sed quia non numquam eius modi tempora incidunt ut labore et dolore magnam aliquam.</p>
  <div class="about-badge" aria-label="Partner badge"></div>
  <span class="about-link">Learn more</span>
  <div class="about-photo" role="img" aria-label="Chef in white uniform cooking at a professional kitchen stove"></div>
</section>

<h2 class="section-title" style="top:1346px">Menu</h2>

<article class="dish" style="left:118px;top:1452px">
  <div class="dish-photo" role="img" aria-label="Pasta with shrimp in a dark bowl" style="background:linear-gradient(135deg,#2a2522,#8a5a2a 55%,#c8702a)"></div>
  <span class="dish-new">New</span>
  <h3 class="dish-name">Lorem Ipsum</h3>
  <p class="dish-desc">Nemo enim ipsam voluptatem quia voluptas</p>
</article>
<article class="dish" style="left:446px;top:1452px">
  <div class="dish-photo" role="img" aria-label="Slice of pizza with roasted peppers on a wooden board" style="background:linear-gradient(135deg,#6a3a1e,#c87a3a 50%,#e8a050)"></div>
  <span class="dish-new">New</span>
  <h3 class="dish-name">Lorem Ipsum</h3>
  <p class="dish-desc">Nemo enim ipsam voluptatem quia voluptas</p>
</article>
<article class="dish" style="left:775px;top:1452px">
  <div class="dish-photo" role="img" aria-label="Chef plating a fine dining dish" style="background:linear-gradient(160deg,#e8e2da,#b8a896 55%,#d8c8b0)"></div>
  <span class="dish-new">New</span>
  <h3 class="dish-name">Lorem Ipsum</h3>
  <p class="dish-desc">Nemo enim ipsam voluptatem quia voluptas</p>
</article>
<article class="dish" style="left:118px;top:1822px">
  <div class="dish-photo" role="img" aria-label="Glazed grilled ribs" style="background:linear-gradient(135deg,#e8a030,#7a3a18 50%,#2a1408)"></div>
  <span class="dish-new">New</span>
  <h3 class="dish-name">Lorem Ipsum</h3>
  <p class="dish-desc">Nemo enim ipsam voluptatem quia voluptas</p>
</article>
<article class="dish" style="left:446px;top:1822px">
  <div class="dish-photo" role="img" aria-label="Appetizer platter with vegetables and dips" style="background:linear-gradient(135deg,#3a2a1a,#8a6a3a 50%,#d8c8a0)"></div>
  <span class="dish-new">New</span>
  <h3 class="dish-name">Lorem Ipsum</h3>
  <p class="dish-desc">Nemo enim ipsam voluptatem quia voluptas</p>
</article>
<article class="dish" style="left:775px;top:1822px">
  <div class="dish-photo" role="img" aria-label="Chocolate dessert with shaved chocolate" style="background:linear-gradient(135deg,#8a6a5a,#4a2a1e 55%,#2a160e)"></div>
  <span class="dish-new">New</span>
  <h3 class="dish-name">Lorem Ipsum</h3>
  <p class="dish-desc">Nemo enim ipsam voluptatem quia voluptas</p>
</article>

<div class="btn-menu">Menu
  <svg width="8" height="12" viewBox="0 0 8 12"><path d="M1 1l5 5-5 5" fill="none" stroke="#1c1c1c" stroke-width="2"/></svg>
</div>

<h2 class="section-title" style="top:2372px">Gallery</h2>

<div class="gallery-tile" style="left:118px;top:2510px;background:linear-gradient(135deg,#e8dccb,#b89a78 60%,#6a4a30)" role="img" aria-label="Cappuccino and pastry"></div>
<div class="gallery-tile" style="left:362px;top:2510px;background:linear-gradient(180deg,#a8c0d8,#d8c8b0 50%,#b87a4a)" role="img" aria-label="Canal-side table with pizza and a drink"></div>
<div class="gallery-tile" style="left:607px;top:2510px;background:linear-gradient(180deg,#5aa8e0,#3a88b8 45%,#d8c8a8)" role="img" aria-label="Coffee on a terrace overlooking a coastal town"></div>
<div class="gallery-tile" style="left:851px;top:2510px;background:linear-gradient(160deg,#a8988a,#6a4a3a 55%,#3a2a22)" role="img" aria-label="Set tables on a restaurant terrace"></div>
<div class="gallery-tile" style="left:118px;top:2731px;background:linear-gradient(160deg,#d8d0c8,#9a8a7a 55%,#5a4a40)" role="img" aria-label="Kitchen brigade at work"></div>
<div class="gallery-tile" style="left:362px;top:2731px;background:linear-gradient(180deg,#4a78c8,#8a5a3a 60%,#c8b8a8)" role="img" aria-label="Chocolate gelato scoop in a cup"></div>
<div class="gallery-tile" style="left:607px;top:2731px;background:linear-gradient(135deg,#2a2a2a,#e8d8a0 45%,#7aa848)" role="img" aria-label="Salad with egg on a white plate"></div>
<div class="gallery-tile" style="left:851px;top:2731px;background:linear-gradient(180deg,#7ab8e0,#c8d8e0 50%,#8a9a6a)" role="img" aria-label="Rooftop terrace with city view"></div>

<section class="booking" role="img" aria-label="Dim restaurant interior with candlelight and glassware, softly blurred">
  <h2 class="booking-title">Book Now</h2>
  <div class="field" style="left:260px;top:184px;width:310px;height:42px">Your Name</div>
  <div class="field" style="left:586px;top:184px;width:312px;height:42px">Email</div>
  <div class="field" style="left:260px;top:234px;width:638px;height:99px">Message</div>
  <div class="btn-submit">Book Now</div>
</section>

<div class="footer-col" style="left:118px">
  <h4>Quick</h4>Home<br>About<br>Menu<br>Gallery<br>Contacts
</div>
<div class="footer-col" style="left:273px">
  <h4>Menu</h4>Pure Veg<br>Pure Non Veg<br>Beverage<br>Ideals Special Food
</div>
<div class="footer-col" style="left:486px">
  <h4>Hours</h4>Weekdays 11 am - late<br>Weekends 11 am - 2 am
  <p style="margin-top:12px">Weekend Brunch<br>Saturday &amp; Sunday<br>11 am - 2 pm</p>
</div>
<div class="footer-col" style="left:720px">
  <h4>Location</h4>
  <p>Italian Restaurant<br>18, Lantaarnsteeg<br>Amsterdam, XXXXX</p>
  <p style="margin-top:8px;font-size:13px">For reservation call<br>+31 20 555 0147</p>
</div>
<div class="footer-col" style="left:937px">
  <h4>Social Connects</h4>
  <div class="social" aria-label="Social links"><span></span><span></span><span></span><span></span></div>
</div>

<footer class="copyright">© COPYRIGHT 2018</footer>

</body>
</html>
```